Maple Ledger Business Card

Colors can be blue, grey and white as you see in the attached logo. Needs to have a spot for name, title, phone, email, address, and website. There also needs to be a spot for an agent's picture.

Contact Information for Business Card

See project description.

Colors

Designer to choose colors to be used in the design.

```html
<!DOCTYPE html>
<html lang="en">
<head>
<meta charset="utf-8">
<title>Maple Ledger Business Card</title>
<link rel="stylesheet" href="https://fonts.googleapis.com/css2?family=Poppins:wght@400;500;600&display=swap">
<style>
  :root {
    --stage: #000000;
    --card: #ffffff;
    --brand-blue: #3777b9;
    --ink-grey: #4a4a4d;
    --rule-grey: #6b6b6e;
    --suit-dark: #1f2533;
    --suit-mid: #3a4256;
  }
  * { margin: 0; padding: 0; box-sizing: border-box; }
  html, body { width: 900px; height: 1200px; overflow: hidden; background: var(--stage); }
  body { position: relative; font-family: "Poppins", sans-serif; }

  .card {
    position: absolute;
    left: 82px;
    width: 733px;
    border-radius: 26px;
    overflow: hidden;
  }
  .card-front { top: 137px; height: 429px; background: var(--card); }
  .card-back { top: 633px; height: 428px; background: var(--brand-blue); }

  .front-band {
    position: absolute; left: 0; right: 0; bottom: 0; height: 14px;
    background: var(--brand-blue);
  }

  .brand {
    position: absolute;
    display: flex; align-items: center; gap: 12px;
    font-weight: 600; letter-spacing: 0.5px; white-space: nowrap;
  }
  .brand-square { width: 30px; height: 30px; }
  .brand-front { left: 44px; top: 140px; font-size: 36px; color: var(--brand-blue); }
  .brand-front .brand-square { background: var(--brand-blue); }
  .brand-back { left: 0; right: 0; top: 178px; justify-content: center; font-size: 44px; color: var(--card); }
  .brand-back .brand-square { width: 36px; height: 36px; background: var(--card); }

  .agent-photo {
    position: absolute; left: 448px; top: 23px; width: 236px; height: 287px;
    background: linear-gradient(180deg, var(--suit-mid) 0%, var(--suit-dark) 100%);
  }

  .agent-name {
    position: absolute; left: 43px; top: 250px;
    font-size: 21px; font-weight: 600; color: var(--brand-blue);
  }
  .agent-title {
    position: absolute; left: 43px; top: 278px;
    font-size: 16px; color: var(--ink-grey);
  }
  .divider {
    position: absolute; left: 43px; top: 309px; width: 647px; height: 2px;
    background: var(--rule-grey);
  }

  .contact-list {
    position: absolute; left: 43px; top: 322px; list-style: none;
    font-size: 16px; color: var(--ink-grey);
  }
  .contact-list li { display: flex; align-items: center; gap: 10px; height: 24px; }
  .contact-list svg { width: 16px; height: 16px; fill: var(--brand-blue); }

  .office-address {
    position: absolute; right: 44px; top: 322px; text-align: right;
    font-size: 16px; line-height: 24px; color: var(--ink-grey); font-style: normal;
  }
</style>
</head>
<body>
  <section class="card card-front">
    <div class="brand brand-front"><span class="brand-square"></span>MAPLE LEDGER</div>

    <div class="agent-photo" role="img" aria-label="Portrait of the agent in a dark suit and red striped tie"></div>

    <h1 class="agent-name">Daniel Whitcombe</h1>
    <p class="agent-title">Managing Director</p>
    <div class="divider"></div>

    <ul class="contact-list">
      <li>
        <svg viewBox="0 0 16 16" aria-hidden="true"><path d="M3.5 1.5l2.3 0 1 3.3-1.6 1.3c.8 1.7 2 2.9 3.7 3.7l1.3-1.6 3.3 1v2.3c0 .8-.7 1.5-1.5 1.5C6.8 13 3 9.2 2 3 2 2.2 2.7 1.5 3.5 1.5z"/></svg>
        555-318-4720
      </li>
      <li>
        <svg viewBox="0 0 16 16" aria-hidden="true"><path d="M1 3.5h14v9H1z M1.8 4.3L8 9l6.2-4.7" fill="none" stroke="#3777b9" stroke-width="0"/><path d="M1 3.5h14v.6L8 9.2 1 4.1z"/><path d="M1 5.3l4.6 3.4L1 12z M15 5.3l-4.6 3.4L15 12z M6.4 9.3L8 10.5l1.6-1.2 4.9 3.2h-13z"/></svg>
        daniel@mapleledger.co
      </li>
      <li>
        <svg viewBox="0 0 16 16" aria-hidden="true"><path d="M8 1a7 7 0 100 14A7 7 0 008 1zm0 1.3c.8 0 1.7 1.4 2 3.7H6c.3-2.3 1.2-3.7 2-3.7zM5.8 2.8C5.2 3.7 4.8 4.8 4.7 6H2.6a5.7 5.7 0 013.2-3.2zm4.4 0A5.7 5.7 0 0113.4 6h-2.1c-.1-1.2-.5-2.3-1.1-3.2zM2.4 7.3h2.2v1.4H2.4zm3.5 0h4.2v1.4H5.9zm5.5 0h2.2v1.4h-2.2zM2.6 10h2.1c.1 1.2.5 2.3 1.1 3.2A5.7 5.7 0 012.6 10zm3.4 0h4c-.3 2.3-1.2 3.7-2 3.7S6.3 12.3 6 10zm5.3 0h2.1a5.7 5.7 0 01-3.2 3.2c.6-.9 1-2 1.1-3.2z"/></svg>
        www.mapleledgerhomes.co
      </li>
    </ul>

    <address class="office-address">
      418 Birchwood Lane SE<br>
      Suite 210, Cedar Falls<br>
      IA 50613
    </address>

    <div class="front-band"></div>
  </section>

  <section class="card card-back">
    <div class="brand brand-back"><span class="brand-square"></span>MAPLE LEDGER</div>
  </section>
</body>
</html>
```